Moms Beyond Gnatflies

My company name is Moms beyond gnatflies. We do residential and commercial mosquito control. See attached brochure and logo.

Target Market(s)

My target market is upper middle class families in the midwestern part of the US.

Requirements
Must have
• Form to collect customer information

```html
<!DOCTYPE html>
<html lang="en">
<head>
<meta charset="utf-8">
<title>Moms Beyond Gnatflies</title>
<link rel="stylesheet" href="https://fonts.googleapis.com/css2?family=Arimo:wght@400;700&family=Noto+Serif:ital,wght@0,400;0,700;1,400&family=Open+Sans:ital,wght@1,800&family=Archivo+Black&display=swap">
<style>
  :root {
    --page: #e4e4e4;
    --ink: #222222;
    --muted: #777777;
    --link: #1f7fd0;
    --blue-dark: #0b4d96;
    --blue-mid: #1f6fc4;
    --blue-light: #3a8ee0;
    --green-top: #b5d419;
    --green-bottom: #7aa80a;
    --green-phone: #159a3c;
    --yellow: #f5ea1e;
    --rule: #c4c4c4;
    --field: #ffffff;
    --field-line: #cccccc;
    --button: #1f66b8;
  }
  * { margin: 0; padding: 0; box-sizing: border-box; }
  html, body { width: 805px; height: 1200px; overflow: hidden; background: var(--page); }
  body { position: relative; font-family: "Noto Serif", serif; color: var(--ink); }
  .abs { position: absolute; }

  .topbar { left: 0; top: 0; width: 805px; height: 51px; }
  .topbar .home-icon { left: 20px; top: 20px; }
  .topbar .site-link { left: 36px; top: 19px; font: 700 9px "Arimo", sans-serif; color: var(--link); text-decoration: underline; }
  .topbar .account { left: 242px; top: 20px; font: 8px "Arimo", sans-serif; color: #555; }
  .topbar .search-label { left: 572px; top: 20px; font: 8px "Arimo", sans-serif; color: #333; }
  .topbar .search-field { left: 608px; top: 16px; width: 164px; height: 17px; background: var(--field); border: 1px solid #aaa; border-radius: 3px; }
  .topbar .search-icon { left: 781px; top: 18px; }

  .masthead { left: 0; top: 51px; width: 805px; height: 265px;
    background: radial-gradient(ellipse at 30% 40%, var(--blue-light), var(--blue-mid) 55%, #1a5fb0 100%);
    border-top: 3px solid var(--blue-dark); border-bottom: 3px solid var(--blue-dark); }
  .brand-box { left: 26px; top: 37px; width: 204px; height: 127px; background: #fff;
    box-shadow: 0 0 14px rgba(255,255,255,.7); display: flex; align-items: center; justify-content: center; text-align: center; }
  .brand-box span { font: 700 22px/1.1 "Arimo", sans-serif; color: #138a2e; }
  .callout { left: 285px; top: 55px; font: italic 800 15px/20px "Open Sans", sans-serif; color: #fff; }
  .phone { left: 272px; top: 130px; font: 31px "Archivo Black", sans-serif; color: #0d0d0d; letter-spacing: 1px; }
  .phone .g { color: var(--green-phone); }
  .phone .w { color: #fff; }
  .web { left: 262px; top: 172px; font: 700 14px "Arimo", sans-serif; color: var(--yellow); }
  .initials { left: 655px; top: 36px; width: 60px; text-align: center; font: 700 58px/60px "Arimo", sans-serif; color: #cfe2fb; }

  .nav { left: 0; top: 319px; width: 805px; height: 40px;
    background: linear-gradient(var(--green-top), var(--green-bottom)); }
  .nav ul { list-style: none; position: absolute; left: 390px; top: 11px; display: flex; }
  .nav li { font: 11px "Arimo", sans-serif; color: #fff; padding: 3px 0; border-left: 1px solid #d7ea7a; text-align: center; }
  .nav li.current { font-weight: 700; }

  .section-title { font: 18px "Arimo", sans-serif; color: var(--ink); }
  .rule { height: 1px; background: var(--rule); }
  .intro { left: 30px; top: 484px; font-size: 12px; color: #888; }
  .body-copy { left: 30px; top: 518px; width: 460px; font-size: 9px; line-height: 16px; }
  .body-copy a { color: var(--link); }
  .dashed { left: 30px; top: 594px; width: 478px; border-top: 1px dashed #aaa; }

  .form-label { left: 40px; font: 700 9px "Noto Serif", serif; color: #444; }
  .form-field { left: 111px; width: 367px; height: 22px; background: var(--field); border: 1px solid var(--field-line); }
  .send { left: 111px; top: 1006px; width: 70px; height: 20px; background: var(--button); border-radius: 2px;
    font: 8px "Arimo", sans-serif; color: #fff; display: flex; align-items: center; justify-content: center; }

  .contact { left: 563px; top: 481px; font-size: 9px; line-height: 16.5px; }
  .contact a { color: var(--link); }
  .quote { left: 563px; top: 710px; width: 200px; font-style: italic; font-size: 10px; line-height: 16px; color: #444; }
  .author { left: 563px; top: 776px; font: 700 9px "Noto Serif", serif; color: #555; }
  .follow-badge { left: 605px; top: 876px; width: 112px; height: 116px;
    background: radial-gradient(circle at 45% 40%, #4fb2ea 0%, #2a8fd3 45%, #8cc63f 70%, rgba(228,228,228,0) 72%); }

  .footer-links { left: 51px; top: 1154px; display: flex; font: 7px "Arimo", sans-serif; }
  .footer-links a { color: var(--link); padding: 0 9px; border-left: 1px solid #999; }
  .footer-links a:first-child { border-left: none; padding-left: 0; }
  .rss { width: 16px; height: 10px; background: #3a7fd0; color: #fff; font: 700 6px "Arimo", sans-serif; border-radius: 2px;
    display: flex; align-items: center; justify-content: center; margin-left: 2px; }
  .copyright { right: 30px; top: 1157px; font: 7px "Arimo", sans-serif; color: #555; }
</style>
</head>
<body>
  <header class="abs topbar">
    <svg class="abs home-icon" width="10" height="9" viewBox="0 0 10 9"><path d="M1 5 L5 1 L9 5 M2.5 4 V8.5 H7.5 V4" fill="none" stroke="#222" stroke-width="1.2"/></svg>
    <a class="abs site-link">www.www.MomsBeyondGnatflies.com.com</a>
    <span class="abs account">Email | Client Login</span>
    <span class="abs search-label">search:</span>
    <div class="abs search-field"></div>
    <svg class="abs search-icon" width="14" height="14" viewBox="0 0 14 14"><circle cx="5.5" cy="5.5" r="4" fill="none" stroke="#999" stroke-width="1.4"/><path d="M8.5 8.5 L13 13" stroke="#999" stroke-width="2"/></svg>
  </header>

  <section class="abs masthead">
    <div class="abs brand-box"><span>Moms Beyond<br>Gnatflies</span></div>
    <p class="abs callout">CALL TODAY TO SCHEDULE AN<br>EVALUATION APPOINTMENT<br>AND BEGIN OPTIMIZING</p>
    <p class="abs phone"><span class="g">555</span><span class="w">.</span><span class="g">204</span><span class="w">.</span>7700</p>
    <p class="abs web">WWW.MOMSBEYONDGNATFLIES.COM</p>
    <p class="abs initials">M<br>B<br>G</p>
  </section>

  <nav class="abs nav">
    <ul>
      <li class="current" style="width:72px">Home</li>
      <li style="width:85px">About us</li>
      <li style="width:79px">Services</li>
      <li style="width:81px">Products</li>
      <li style="width:88px">Contact us</li>
    </ul>
  </nav>

  <main>
    <h2 class="abs section-title" style="left:30px;top:437px">Header</h2>
    <div class="abs rule" style="left:30px;top:465px;width:472px"></div>
    <p class="abs intro">Simply dummy text of the printing and typesetting industry.</p>
    <p class="abs body-copy">Lorem Ipsum has been the standard dummy text ever since thes, when an unknown.<br>&nbsp;printer.Simply dummy text of the <a>printing and typesetting industry</a>. Lorem Ipsum has been the industry's standard dummy text ever since thes, when.</p>
    <div class="abs dashed"></div>

    <form>
      <label class="abs form-label" style="top:643px">Name:</label>
      <div class="abs form-field" style="top:640px"></div>
      <label class="abs form-label" style="top:678px">Email:</label>
      <div class="abs form-field" style="top:675px"></div>
      <label class="abs form-label" style="top:713px">Subject:</label>
      <div class="abs form-field" style="top:709px"></div>
      <label class="abs form-label" style="top:748px">Message:</label>
      <div class="abs form-field" style="top:741px;height:258px"></div>
      <div class="abs send">Send Message</div>
    </form>
  </main>

  <aside>
    <h2 class="abs section-title" style="left:564px;top:437px">Get in touch!</h2>
    <div class="abs rule" style="left:553px;top:465px;width:206px"></div>
    <p class="abs contact"><b>Address:</b> 27 Meadow Lane, Elmfield, 14<br><b>Telephone:</b> +555-0142-7788<br><b>FAX:</b> +555-0199<br><b>Others:</b> +555 - 0163 - 02471<br><b>E-mail:</b> <a>hello@momsbeyondgnatflies.com</a></p>

    <h2 class="abs section-title" style="left:564px;top:652px">Testimonials</h2>
    <div class="abs rule" style="left:553px;top:680px;width:206px"></div>
    <p class="abs quote">“Lorem Ipsum is simply dummy text of the printing and typesetting industry. Lorem Ipsum has been the. industry's”</p>
    <p class="abs author">-Dana Whitfield, web designer</p>
    <div class="abs follow-badge" role="img" aria-label="Follow us illustration: cartoon bird holding a green follow sign"></div>
  </aside>

  <footer>
    <div class="abs footer-links"><a>home</a><a>services</a><a>products</a><a>about</a><a>contact</a><a>rss feed</a><span class="rss">RSS</span></div>
    <p class="abs copyright">© Copyright 20011. MomsBeyondGnatflies.com. All Rights Reserved</p>
  </footer>
</body>
</html>
```